Recruitment website for new startup company - Calder Ashby Recruitment

Hi , I need to design a web page for my new recruitment company with the ability to link to social media accounts. The ability to add and remove job posts along with a blog page which I can update. More importantly I need the website to have the functionality of applicants being able to upload their cv and somewhere for me to store it. I will need assistance/recommendation for email address with company name, hosting and security. An about us page. The website will also need a search function for applicants to narrow down the search. Again I will need to be able to update this myself as the company grows. I have my logo ready domain address ready and would like the web site done ASAP. Thank you for your help.
Updates

Reason: Want to get a few more ideas and variations to designs done. But using logo as inspiration Thanks

Target Market(s)

Financial and property industry so professionals. New starters to senior management age range 25-60

Industry/Entity Type

Financial

Coding

Coded - Design and coding required

Number of Pages Required

4 page

Colors

Designer to choose colors to be used in the design.

Requirements
Must have
• Ability for me to add amend and remove job posts, ability for applicants to upload cv and for me to store and access it. Link to social media accounts
Should not have
• Needs to be clean approachable so not to childish but must come across as approachable and trustworthy.
• No yellow please my logo has a gold V not yellow. If it looks yellow use a different colour please. Thanks

```html
<!DOCTYPE html>
<html lang="en">
<head>
<meta charset="utf-8">
<title>Jobs &amp; Vacancies — Calder Ashby Recruitment</title>
<link rel="stylesheet" href="https://fonts.googleapis.com/css2?family=Montserrat:wght@400;500;600;700&display=swap">
<style>
  :root {
    --ink: #222427;
    --text: #3c3d40;
    --muted: #8a8b8e;
    --line: #e8e8e8;
    --navy: #1b3766;
    --footer: #1e1f21;
    --footer-text: #9a9b9e;
    --link: #1d3a6b;
    --placeholder: #f1f1f1;
  }
  * { box-sizing: border-box; margin: 0; padding: 0; }
  html, body {
    width: 1200px; height: 756px; overflow: hidden;
    background: #fff;
    font-family: "Montserrat", Arial, sans-serif;
    color: var(--text);
  }
  .page { position: relative; width: 1200px; height: 756px; }

  /* Sidebar */
  .search {
    position: absolute; left: 93px; top: 81px; width: 230px; height: 34px;
    border: 1px solid var(--line);
    display: flex; align-items: center; justify-content: space-between;
    padding: 0 11px 0 10px;
    font-size: 12px; color: var(--muted);
  }
  .filters {
    position: absolute; left: 93px; top: 124px; width: 230px; height: 507px;
    border: 1px solid var(--line); border-bottom: none;
  }
  .filter-group { padding: 13px 17px 0 17px; border-bottom: 1px solid var(--line); }
  .filter-group:last-child { border-bottom: none; }
  .filter-title {
    font-size: 11.5px; font-weight: 500; color: var(--ink);
    letter-spacing: 0.2px; margin-bottom: 6px;
  }
  .option {
    display: flex; align-items: center; height: 25.3px;
    font-size: 11.5px; color: var(--text);
  }
  .radio {
    width: 15px; height: 15px; border-radius: 50%;
    border: 1px solid #dcdcdc; margin-right: 12px; flex: none;
    display: flex; align-items: center; justify-content: center;
  }
  .radio.checked { border-color: #666; }
  .radio.checked::after { content: ""; width: 7px; height: 7px; border-radius: 50%; background: #555; }
  .box { width: 15px; height: 15px; border: 1px solid #dcdcdc; margin-right: 12px; flex: none; }
  .count { margin-left: auto; font-size: 11px; color: var(--muted); margin-right: 13px; align-self: flex-start; padding-top: 3px; }
  .date-group { height: 193px; }
  .type-group { height: 67px; padding-top: 12px; }
  .type-group .option { padding-left: 27px; }
  .spec-group { padding-top: 13px; }
  .spec-group .option { height: 25.7px; }

  /* Listing */
  .listing-heading {
    position: absolute; left: 350px; top: 88px;
    font-size: 20px; font-weight: 600; color: var(--text); letter-spacing: 0.2px;
  }
  .job-thumb {
    position: absolute; left: 368px; top: 143px; width: 117px; height: 88px;
    border: 1px solid var(--line); background: var(--placeholder);
  }
  .job-title {
    position: absolute; left: 521px; top: 148px;
    font-size: 14.5px; font-weight: 600; color: var(--ink); letter-spacing: 0.6px;
  }
  .job-meta { position: absolute; left: 521px; top: 182px; font-size: 10px; }
  .job-meta div { display: flex; height: 19px; align-items: center; }
  .job-meta dt { width: 95px; color: var(--ink); }
  .job-meta dd { color: var(--muted); }
  .job-excerpt {
    position: absolute; left: 521px; top: 251px;
    font-size: 12px; color: var(--ink); display: flex; align-items: center;
  }
  .read-more {
    margin-left: 8px; font-size: 8.5px; font-weight: 700; letter-spacing: 1px;
    color: var(--ink); display: flex; align-items: center; gap: 7px;
  }
  .tag {
    position: absolute; left: 889px; top: 143px; width: 125px; height: 26px;
    border: 1px solid #6a6a6a;
    display: flex; align-items: center; justify-content: center;
    font-size: 9.5px; font-weight: 600; letter-spacing: 1px; color: #555;
  }
  .save {
    position: absolute; left: 1019px; top: 143px; width: 29px; height: 26px;
    background: var(--navy); display: flex; align-items: center; justify-content: center;
  }

  /* Footer */
  .site-footer {
    position: absolute; left: 0; top: 685px; width: 1200px; height: 71px;
    background: var(--footer);
  }
  .copyright { position: absolute; left: 93px; top: 26px; font-size: 11.5px; color: var(--footer-text); }
  .back-top {
    position: absolute; left: 1006px; top: 30px;
    display: flex; align-items: center; gap: 8px;
    font-size: 11.5px; color: var(--link);
  }
  .back-top span.dot {
    width: 17px; height: 17px; border-radius: 50%; background: var(--navy);
    display: flex; align-items: center; justify-content: center;
  }
</style>
</head>
<body>
<div class="page">

  <aside>
    <div class="search">
      <span>Job title</span>
      <svg width="12" height="12" viewBox="0 0 12 12" aria-hidden="true">
        <circle cx="5" cy="5" r="3.8" fill="none" stroke="#999" stroke-width="1.6"/>
        <line x1="7.8" y1="7.8" x2="11" y2="11" stroke="#999" stroke-width="1.8"/>
      </svg>
    </div>

    <div class="filters">
      <div class="filter-group date-group">
        <h3 class="filter-title">DATE POSTED</h3>
        <div class="option"><span class="radio"></span>Last Hour</div>
        <div class="option"><span class="radio"></span>Last 24 hours</div>
        <div class="option"><span class="radio"></span>Last 7 days</div>
        <div class="option"><span class="radio"></span>Last 14 days</div>
        <div class="option"><span class="radio"></span>Last 30 days</div>
        <div class="option"><span class="radio checked"></span>All</div>
      </div>
      <div class="filter-group type-group">
        <h3 class="filter-title">VACANCY TYPE</h3>
        <div class="option">Finance Related<span class="count">(1)</span></div>
      </div>
      <div class="filter-group spec-group">
        <h3 class="filter-title">SPECIALISMS</h3>
        <div class="option"><span class="box"></span>Accountants<span class="count">(0)</span></div>
        <div class="option"><span class="box"></span>Back Office staff<span class="count">(0)</span></div>
        <div class="option"><span class="box"></span>Banking<span class="count">(0)</span></div>
        <div class="option"><span class="box"></span>Bridging finance<span class="count">(0)</span></div>
        <div class="option"><span class="box"></span>Commercial advisers<span class="count">(0)</span></div>
        <div class="option"><span class="box"></span>Directors/managers<span class="count">(0)</span></div>
        <div class="option"><span class="box"></span>Equity release<span class="count">(0)</span></div>
        <div class="option"><span class="box"></span>More</div>
      </div>
    </div>
  </aside>

  <main>
    <h1 class="listing-heading">1 Jobs &amp; Vacancies</h1>

    <article>
      <div class="job-thumb" role="img" aria-label="Job thumbnail placeholder: no image available"></div>
      <h2 class="job-title">INSURANCE SPECIALISTS</h2>
      <dl class="job-meta">
        <div><dt>Posted</dt><dd>3 weeks ago</dd></div>
        <div><dt>Specialism</dt><dd>Insurance Specialists</dd></div>
        <div><dt>Location</dt><dd>London</dd></div>
      </dl>
      <p class="job-excerpt">Insurance Specialists
        <span class="read-more">READ MORE
          <svg width="5" height="8" viewBox="0 0 5 8" aria-hidden="true"><path d="M1 1l3 3-3 3" fill="none" stroke="#999" stroke-width="1.2"/></svg>
        </span>
      </p>
      <span class="tag">FINANCE RELATED</span>
      <span class="save" aria-label="Save job">
        <svg width="13" height="12" viewBox="0 0 13 12" aria-hidden="true">
          <path d="M6.5 11S1 7.4 1 3.9A2.6 2.6 0 0 1 6.5 2.6 2.6 2.6 0 0 1 12 3.9C12 7.4 6.5 11 6.5 11z" fill="none" stroke="#fff" stroke-width="1.2"/>
        </svg>
      </span>
    </article>
  </main>

  <footer class="site-footer">
    <p class="copyright">© 2017 Calder Ashby All rights reserved.</p>
    <a class="back-top">Back to top
      <span class="dot"><svg width="7" height="5" viewBox="0 0 7 5" aria-hidden="true"><path d="M3.5 0L7 5H0z" fill="#fff"/></svg></span>
    </a>
  </footer>

</div>
</body>
</html>
```